A start-up named "brivora" - a clinical research organization needs a new PowerPoint design

We need a new PowerPoint Design (incl. business card and stationery design) for an early-stage start-up named "brivora" seeking to build an ecosystem/ strategic partner alliances or consortium of committed and active collaborators to guide important components of the clinical trial.

Our ultimate goal is to avoid false neutrals – therapies that have not been and may never be evaluated in clinical trials due to the costs and/ or complexity.

The final design should highlight our patient-centric approach, innovative study design supported with the novel AI platform to make a stronger impact on patient lives.

Please see the attached brief for more details.
Updates

Requesting the proposals on color-coding, business-card designs, clinical research visuals, and icons as well as stationery design.

Target Market(s)

Pharma/ Biotech Executives
Medical Institutions
Clinical Trial Participants (Patients)

Colors
e34398

Requirements
Must have
• Use the Color Version of purple/ magenta logo

```html
<!DOCTYPE html>
<html lang="en">
<head>
<meta charset="utf-8">
<title>brivora – Organisation / Who we are</title>
<link href="https://fonts.googleapis.com/css2?family=Open+Sans:wght@400;600;700&display=swap" rel="stylesheet">
<style>
  :root {
    --brand-magenta: #e34398;
    --brand-magenta-deep: #d42f86;
    --panel-tint: #e0479a;
    --ink: #1f1f1f;
    --body-ink: #2b2b2b;
    --white: #ffffff;
    --rule: #d6d6d6;
    --callout-bg: #d9dadf;
    --badge-bg: #d9d9dc;
    --icon-science: #c43bd3;
    --icon-idea: #4aa6e0;
    --icon-alert: #8b6fe0;
  }
  * { box-sizing: border-box; margin: 0; padding: 0; }
  html, body { width: 1200px; height: 675px; overflow: hidden; background: var(--white); }
  body { font-family: "Open Sans", Arial, sans-serif; }

  .slide { position: relative; width: 1200px; height: 675px; overflow: hidden; background: var(--white); }

  .intro-panel {
    position: absolute; left: 0; top: 0; width: 413px; height: 675px;
    background: linear-gradient(160deg, #e65aa5 0%, var(--panel-tint) 45%, var(--brand-magenta-deep) 100%);
    color: var(--white);
  }
  .intro-panel__photo {
    position: absolute; inset: 0;
    background:
      radial-gradient(ellipse 120px 220px at 330px 560px, rgba(255,255,255,0.10), transparent 70%),
      radial-gradient(ellipse 90px 200px at 60px 600px, rgba(120,20,70,0.12), transparent 70%),
      radial-gradient(ellipse 200px 160px at 300px 80px, rgba(255,255,255,0.08), transparent 70%);
  }
  .intro-panel__title {
    position: absolute; left: 56px; top: 70px;
    font-size: 42px; font-weight: 700; line-height: 49px;
    text-shadow: 0 2px 4px rgba(90,0,50,0.35);
  }
  .intro-panel__rule { position: absolute; left: 57px; top: 175px; width: 40px; height: 3px; background: var(--white); }
  .intro-panel__text {
    position: absolute; left: 56px; top: 234px;
    font-size: 24px; line-height: 30px; font-weight: 400; letter-spacing: -0.4px;
    white-space: nowrap;
  }
  .intro-panel__text strong { font-weight: 700; }

  .brand-name {
    position: absolute; left: 56px; top: 596px;
    font-size: 30px; font-weight: 700; color: var(--white); line-height: 1;
  }

  .point { position: absolute; left: 469px; display: flex; align-items: center; }
  .point__icon { width: 96px; height: 96px; flex: none; }
  .point__text {
    margin-left: 35px; font-size: 19.5px; line-height: 24.5px; color: var(--body-ink);
    white-space: nowrap;
  }
  .point__text strong { font-weight: 700; color: var(--ink); }
  .point--science { top: 81px; }
  .point--balance { top: 224px; }
  .point--focus { top: 378px; }

  .divider { position: absolute; left: 600px; width: 548px; height: 1px; background: var(--rule); }
  .divider--one { top: 188px; }
  .divider--two { top: 355px; }

  .callout {
    position: absolute; left: 470px; top: 535px; width: 678px; height: 49px;
    background: var(--callout-bg); border-radius: 6px;
    box-shadow: 0 2px 0 #c3c4c9;
    display: flex; align-items: center; justify-content: center;
    font-size: 19.5px; font-weight: 700; color: var(--ink);
  }
  .callout span { font-weight: 400; }

  .page-badge {
    position: absolute; left: 1101px; top: 601px; width: 42px; height: 42px; border-radius: 50%;
    background: var(--badge-bg); display: flex; align-items: center; justify-content: center;
    font-size: 15px; font-weight: 700; color: var(--ink);
  }
</style>
</head>
<body>
<div class="slide">
  <section class="intro-panel">
    <div class="intro-panel__photo" role="img" aria-label="Photo of people walking through a bright corridor, tinted magenta"></div>
    <h1 class="intro-panel__title">Organisation/<br>Who we are</h1>
    <div class="intro-panel__rule"></div>
    <p class="intro-panel__text">BRIVORA is an early-<br>stage start-up seeking to<br><strong>build an ecosystem/<br>strategic partner<br>alliances</strong> or consortium<br>of committed and active<br>collaborators to guide<br>important components of<br>the clinical trial</p>
    <div class="brand-name">brivora</div>
  </section>

  <div class="point point--science">
    <svg class="point__icon" viewBox="0 0 96 96" aria-hidden="true">
      <circle cx="48" cy="48" r="48" fill="var(--icon-science)"/>
      <g fill="none" stroke="#fff" stroke-width="1.6" stroke-linecap="round">
        <rect x="28" y="30" width="40" height="28" rx="1.5"/>
        <line x1="48" y1="58" x2="48" y2="65"/><line x1="39" y1="66" x2="57" y2="66"/>
        <ellipse cx="48" cy="44" rx="11" ry="4.5"/>
        <ellipse cx="48" cy="44" rx="11" ry="4.5" transform="rotate(60 48 44)"/>
        <ellipse cx="48" cy="44" rx="11" ry="4.5" transform="rotate(-60 48 44)"/>
      </g>
      <circle cx="48" cy="44" r="1.8" fill="#fff"/>
    </svg>
    <p class="point__text">The Science around new medical treatments is rapidly<br>progressing, but there are many questions surrounding<br><strong>how Science could Translate into a Therapy.</strong></p>
  </div>

  <div class="divider divider--one"></div>

  <div class="point point--balance">
    <svg class="point__icon" viewBox="0 0 96 96" aria-hidden="true">
      <circle cx="48" cy="48" r="48" fill="var(--icon-idea)"/>
      <g fill="none" stroke="#fff" stroke-width="1.6" stroke-linecap="round">
        <path d="M41 58 C41 52 36 49 36 42 A12 12 0 0 1 60 42 C60 49 55 52 55 58 Z"/>
        <line x1="42" y1="62" x2="54" y2="62"/><line x1="44" y1="66" x2="52" y2="66"/>
        <line x1="48" y1="20" x2="48" y2="25"/>
        <line x1="30" y1="28" x2="33" y2="31"/><line x1="66" y1="28" x2="63" y2="31"/>
        <line x1="23" y1="42" x2="28" y2="42"/><line x1="68" y1="42" x2="73" y2="42"/>
        <line x1="30" y1="56" x2="33" y2="53"/><line x1="66" y1="56" x2="63" y2="53"/>
      </g>
    </svg>
    <p class="point__text">Success lies in moving from an idea generating phase at<br>a 50.000-foot level to the on-the ground implementation<br>phase. It is crucial to strike a balance between what is<br><strong>scientifically valuable and operationally feasible</strong></p>
  </div>

  <div class="divider divider--two"></div>

  <div class="point point--focus">
    <svg class="point__icon" viewBox="0 0 96 96" aria-hidden="true">
      <circle cx="48" cy="48" r="48" fill="var(--icon-alert)"/>
      <g fill="none" stroke="#fff" stroke-width="1.6" stroke-linecap="round" stroke-linejoin="round">
        <path d="M48 28 L70 66 L26 66 Z"/>
        <line x1="48" y1="42" x2="48" y2="55"/>
      </g>
      <circle cx="48" cy="60" r="1.4" fill="#fff"/>
    </svg>
    <p class="point__text">We have no time or money to spend on wasted efforts. We<br>really need to focus on tasks where we/ patients could<br>gain something. We have to figure out how we can best<br>use science at our disposal to avoid type 1 error but also<br><strong>get superior treatments to patients.</strong></p>
  </div>

  <div class="callout">…therefore, we strive to work brivora&nbsp;<span>(for sapiens)</span></div>

  <div class="page-badge">7</div>
</div>
</body>
</html>
```